New business card design needed for Trucking/Staffing company!

I am looking for a business card design. The business name is Keystone Haul Partners, LLC. This company is a staffing company for commercial drivers/truck drivers. Most of our customers are trucking/supply companies. Our colors are blue/black/white/grey. The info I have on my current business cards is
-Spot for a name
-2 lines for an address
-3 lines for Office, cell, and fax
-email
-website(currently on backside of card with logo but can go anywhere)
Updates

Project Deadline Extended
Reason: Open to more designs

Target Market(s)

Trucking companies, building supply companies

Industry/Entity Type

Business

Contact Information for Business Card

Edgy but professional

Font styles to use
Other font styles liked:
• Open to suggestions

Colors
0555a3
000000
ffffff
9d9d9d

Requirements
Must have
• Must have the logo incorporated

```html
<!DOCTYPE html>
<html lang="en">
<head>
<meta charset="utf-8">
<title>Keystone Haul Partners – Business Card</title>
<link href="https://fonts.googleapis.com/css2?family=Arimo:wght@400;700&display=swap" rel="stylesheet">
<style>
  :root {
    --brand-blue: #1a2cff;
    --deep-blue: #0555a3;
    --card-black: #050505;
    --card-sheen: #1c1c1c;
    --white: #ffffff;
    --grey: #9d9d9d;
    --backdrop: #d9d9d6;
  }
  * { margin: 0; padding: 0; box-sizing: border-box; }
  html, body {
    width: 1200px; height: 892px; overflow: hidden;
    background: var(--backdrop);
    font-family: "Arimo", Arial, sans-serif;
  }
  .sheet {
    position: relative; width: 1200px; height: 892px;
    display: flex; flex-direction: column; align-items: center; justify-content: center; gap: 32px;
  }
  .card {
    position: relative; width: 700px; height: 400px;
    background: linear-gradient(135deg, var(--card-sheen) 0%, var(--card-black) 45%, var(--card-black) 70%, #141414 100%);
    color: var(--white);
    box-shadow: 0 10px 24px rgba(0,0,0,0.25);
    overflow: hidden;
  }

  /* Front */
  .front-brand {
    position: absolute; left: 40px; top: 0; bottom: 0; width: 270px;
    display: flex; align-items: center; gap: 12px;
  }
  .brand-mark {
    width: 14px; height: 14px; flex: none; background: var(--brand-blue);
  }
  .brand-name {
    font-weight: 700; font-size: 30px; line-height: 1.1; letter-spacing: 1px;
    text-transform: uppercase; color: var(--brand-blue);
  }
  .divider {
    position: absolute; left: 330px; top: 34px; bottom: 34px; width: 2px;
    background: var(--brand-blue);
  }
  .person {
    position: absolute; left: 360px; top: 48px;
  }
  .person-name {
    font-size: 30px; font-weight: 400; color: var(--brand-blue); line-height: 1.1;
  }
  .person-title {
    font-size: 21px; color: var(--white); margin-top: 4px;
  }
  .contact-list {
    position: absolute; left: 360px; top: 168px; list-style: none;
  }
  .contact-item {
    display: flex; align-items: flex-start; gap: 12px;
    font-size: 17px; line-height: 20px; margin-bottom: 13px; color: var(--white);
  }
  .contact-icon {
    width: 18px; height: 18px; flex: none; margin-top: 1px;
  }

  /* Back */
  .back {
    display: flex; flex-direction: column; align-items: center; justify-content: center; gap: 26px;
  }
  .back .brand {
    display: flex; align-items: center; gap: 16px;
  }
  .back .brand-mark { width: 20px; height: 20px; background: var(--white); }
  .back .brand-name {
    color: var(--white); font-size: 44px; letter-spacing: 2px; text-align: center;
  }
  .back-website {
    font-size: 26px; color: var(--brand-blue);
  }
</style>
</head>
<body>
<main class="sheet">

  <section class="card front" aria-label="Business card front">
    <div class="front-brand">
      <span class="brand-mark"></span>
      <span class="brand-name">Keystone Haul<br>Partners</span>
    </div>
    <div class="divider"></div>
    <div class="person">
      <p class="person-name">Dara Whitcombe</p>
      <p class="person-title">Managing Director</p>
    </div>
    <ul class="contact-list">
      <li class="contact-item">
        <svg class="contact-icon" viewBox="0 0 18 18" aria-hidden="true"><rect width="18" height="18" fill="#fff"/><path d="M5 4h2.5l1 3-1.5 1a6 6 0 0 0 3 3l1-1.5 3 1V13c0 .6-.5 1-1 1A9 9 0 0 1 4 5c0-.6.4-1 1-1z" fill="#000"/></svg>
        <span>(555) 210-4817</span>
      </li>
      <li class="contact-item">
        <svg class="contact-icon" viewBox="0 0 18 18" aria-hidden="true"><rect width="18" height="18" fill="#fff"/><rect x="4" y="4" width="10" height="10" fill="none" stroke="#000" stroke-width="1.6"/><rect x="6" y="3" width="6" height="4" fill="#000"/><rect x="6" y="9" width="6" height="3" fill="#000"/></svg>
        <span>(555) 210-4830</span>
      </li>
      <li class="contact-item">
        <svg class="contact-icon" viewBox="0 0 18 18" aria-hidden="true"><rect width="18" height="18" fill="#fff"/><rect x="3.5" y="5" width="11" height="8" fill="none" stroke="#000" stroke-width="1.5"/><path d="M3.5 5l5.5 4.5L14.5 5" fill="none" stroke="#000" stroke-width="1.5"/></svg>
        <span>info@keystonehaulpartners.com</span>
      </li>
      <li class="contact-item">
        <svg class="contact-icon" viewBox="0 0 18 18" aria-hidden="true"><rect width="18" height="18" fill="#fff"/><circle cx="9" cy="9" r="5.5" fill="none" stroke="#000" stroke-width="1.4"/><ellipse cx="9" cy="9" rx="2.3" ry="5.5" fill="none" stroke="#000" stroke-width="1.2"/><path d="M3.5 9h11" stroke="#000" stroke-width="1.2"/></svg>
        <span>www.keystonehaulpartners.com</span>
      </li>
      <li class="contact-item">
        <svg class="contact-icon" viewBox="0 0 18 18" aria-hidden="true"><rect width="18" height="18" fill="#fff"/><path d="M9 15s-4-4.3-4-7.2a4 4 0 0 1 8 0C13 10.7 9 15 9 15z" fill="#000"/><circle cx="9" cy="7.8" r="1.5" fill="#fff"/></svg>
        <span>418 N. Ridgeline Road, Suite<br>112 Harlow Springs, CA 90417</span>
      </li>
    </ul>
  </section>

  <section class="card back" aria-label="Business card back">
    <div class="brand">
      <span class="brand-mark"></span>
      <span class="brand-name">KEYSTONE HAUL<br>PARTNERS</span>
    </div>
    <p class="back-website">www.keystonehaulpartners.com</p>
  </section>

</main>
</body>
</html>
```